Web Design Business Card

I need a new business card designed, we recently rebranded and I need to get a fresh design to match our new logo, colours and branding.

Details:

Dorian Keeble | Founder & CEO
Address: 7 Fernhollow Lane, #04-09 Maplecrest Vale, Singapore 583104
Tel: +65 93468120
Web: www.plumtrove.com.sg
hello@plumtrove.com.sg

I've attached my old card as well

Requirements
Must have
• Front and Back
Interesting use of logo
Correct use of colour scheme

```html
<!DOCTYPE html>
<html lang="en">
<head>
<meta charset="utf-8">
<title>Plumtrove Business Card – Front and Back</title>
<link rel="stylesheet" href="https://fonts.googleapis.com/css2?family=Open+Sans:wght@300;400;700&family=Arimo:wght@400&display=swap">
<style>
  :root {
    --backdrop: #e9e7e4;
    --card: #ffffff;
    --card-shade: #f1f1f1;
    --ink: #111111;
    --title-grey: #9a9a9a;
    --brand-blue: #1aa3e8;
    --sky-light: #c4e9fb;
    --sky-mid: #7fd0f4;
    --taupe: #a89a93;
    --umber: #6d5f58;
    --brand-brown: #7a6a62;
  }
  * { box-sizing: border-box; margin: 0; padding: 0; }
  html, body {
    width: 1200px;
    height: 900px;
    overflow: hidden;
    background: var(--backdrop);
  }
  .sheet {
    width: 1200px;
    height: 900px;
    display: flex;
    align-items: center;
    justify-content: center;
    gap: 60px;
  }
  .card {
    position: relative;
    width: 520px;
    height: 300px;
    background: linear-gradient(180deg, var(--card) 0%, var(--card) 55%, var(--card-shade) 100%);
    box-shadow: 0 6px 18px rgba(0,0,0,0.18);
    overflow: hidden;
    font-family: "Open Sans", sans-serif;
  }
  .brand {
    display: flex;
    align-items: center;
    gap: 10px;
  }
  .brand-dot {
    width: 44px;
    height: 44px;
    border-radius: 50%;
    background: var(--brand-blue);
    flex: none;
  }
  .brand-name {
    font-family: "Open Sans", sans-serif;
    font-weight: 700;
    font-size: 30px;
    letter-spacing: -0.5px;
    color: var(--brand-brown);
  }
  .card-front .brand {
    position: absolute;
    left: 36px;
    top: 38px;
  }
  .identity {
    position: absolute;
    left: 36px;
    top: 142px;
    font-size: 22px;
    line-height: 30px;
    white-space: nowrap;
  }
  .identity .person { color: var(--ink); font-weight: 400; }
  .identity .divider { color: var(--brand-blue); font-weight: 300; margin: 0 4px; }
  .identity .role { color: var(--title-grey); font-weight: 300; }
  .contact-list,
  .address {
    position: absolute;
    font-family: "Arimo", sans-serif;
    font-size: 13px;
    color: var(--ink);
    line-height: 18px;
  }
  .contact-list {
    left: 40px;
    top: 188px;
    display: grid;
    grid-template-columns: 48px auto;
  }
  .address {
    left: 282px;
    top: 80px;
    display: grid;
    grid-template-columns: 62px 12px auto;
  }
  .address .label { align-self: end; grid-row: 1 / 4; padding-bottom: 18px; }
  .address .colon { grid-row: 1; }
  .bottom-band {
    position: absolute;
    left: 0;
    bottom: 0;
    width: 520px;
    height: 300px;
  }
  .card-back {
    display: flex;
    align-items: center;
    justify-content: center;
  }
</style>
</head>
<body>
<main class="sheet">
  <section class="card card-front" aria-label="Business card front">
    <div class="brand">
      <span class="brand-dot"></span>
      <span class="brand-name">plumtrove</span>
    </div>

    <div class="address">
      <span class="label">Address</span><span class="colon">:</span>
      <span>7 Fernhollow Lane,<br>#04-09 Maplecrest Vale,<br>Singapore 583104</span>
    </div>

    <p class="identity">
      <span class="person">Dorian Keeble</span><span class="divider">|</span><span class="role">Founder &amp; CEO</span>
    </p>

    <div class="contact-list">
      <span>Tel</span><span>: +65 93468120</span>
      <span>Web</span><span>: www.plumtrove.com.sg</span>
      <span>e-mail</span><span>: hello@plumtrove.com.sg</span>
    </div>

    <svg class="bottom-band" viewBox="0 0 520 300" aria-hidden="true">
      <defs>
        <linearGradient id="band-sky" x1="0" y1="0" x2="1" y2="0">
          <stop offset="0" stop-color="var(--sky-light)"/>
          <stop offset="1" stop-color="var(--sky-mid)"/>
        </linearGradient>
      </defs>
      <polygon points="0,288 520,255 520,288" fill="url(#band-sky)"/>
      <polygon points="400,262.6 430,260.7 430,272 400,272" fill="var(--sky-mid)"/>
      <polygon points="430,260.7 460,258.8 460,272 430,272" fill="var(--brand-blue)"/>
      <polygon points="460,258.8 490,256.9 490,272 460,272" fill="var(--taupe)"/>
      <polygon points="490,256.9 520,255 520,272 490,272" fill="var(--umber)"/>
      <rect x="0" y="288" width="520" height="12" fill="var(--brand-blue)"/>
    </svg>
  </section>

  <section class="card card-back" aria-label="Business card back">
    <div class="brand">
      <span class="brand-dot"></span>
      <span class="brand-name">plumtrove</span>
    </div>
  </section>
</main>
</body>
</html>
```